Need Business Card for our Indian Grocery Store

Industry/Entity Type

Grocery Store

Contact Information for Business Card

Manoj Baweja
Director

Store Locations:

Brindlewood
482 Elm Parade
P: 03 9172 5843

Kestrelton
613 Carlow Road
P: 03 9238 6014

email: kvtmarts@mailnest.example

Requirements
Must have
• Our logo Colours

```html
<!DOCTYPE html>
<html lang="en">
<head>
<meta charset="utf-8">
<title>KVT Groceries &amp; Spices – Business Card</title>
<link href="https://fonts.googleapis.com/css2?family=Montserrat:wght@400;700;800&display=swap" rel="stylesheet">
<style>
  :root {
    --stage: #000000;
    --paper: #f7f7f5;
    --brand-red: #df1f26;
    --ink: #111111;
    --on-red: #ffffff;
  }
  * { box-sizing: border-box; margin: 0; padding: 0; }
  html, body { width: 1200px; height: 857px; overflow: hidden; background: var(--stage); }
  body { position: relative; font-family: "Montserrat", sans-serif; }

  .card {
    position: absolute;
    top: 277px;
    background: var(--paper);
    border-radius: 14px;
    overflow: hidden;
  }
  .card--front { left: 45px; width: 546px; height: 313px; }
  .card--back { left: 620px; width: 551px; height: 315px; }

  .brand {
    position: absolute;
    display: flex;
    align-items: center;
    color: var(--brand-red);
    font-weight: 800;
    letter-spacing: 0.02em;
    white-space: nowrap;
  }
  .brand__mark { background: var(--brand-red); flex: none; }

  .brand--small { left: 19px; top: 40px; font-size: 13px; gap: 7px; }
  .brand--small .brand__mark { width: 24px; height: 24px; }

  .brand--large { left: 0; right: 0; top: 126px; justify-content: center; font-size: 28px; gap: 14px; }
  .brand--large .brand__mark { width: 48px; height: 48px; }

  .person { position: absolute; left: 368px; top: 19px; }
  .person__name { font-size: 16px; font-weight: 800; letter-spacing: 0.08em; color: var(--ink); text-transform: uppercase; }
  .person__role { font-size: 12.5px; font-weight: 700; letter-spacing: 0.05em; color: var(--brand-red); margin-top: 1px; }

  .locations-band {
    position: absolute; left: 0; right: 0; top: 157px; height: 137px;
    background: var(--brand-red); color: var(--on-red);
  }
  .store { position: absolute; top: 37px; font-size: 13px; letter-spacing: 0.08em; line-height: 18.5px; }
  .store__heading { font-size: 16px; font-weight: 800; letter-spacing: 0.1em; text-transform: uppercase; line-height: 20px; margin-bottom: 2px; }
  .store--first { left: 20px; }
  .store--second { right: 20px; top: 40px; text-align: right; }

  .email-band {
    position: absolute; left: 0; right: 0; bottom: 0; height: 37px;
    background: var(--brand-red); color: var(--on-red);
    text-align: center; font-size: 12.5px; font-weight: 700; letter-spacing: 0.07em;
    padding-top: 2px;
  }
</style>
</head>
<body>
  <section class="card card--front" aria-label="Business card front">
    <div class="brand brand--small"><span class="brand__mark"></span>KVT Groceries &amp; Spices</div>
    <div class="person">
      <p class="person__name">Manoj Baweja</p>
      <p class="person__role">Director</p>
    </div>
    <div class="locations-band">
      <div class="store store--first">
        <p class="store__heading">Store Locations :</p>
        <p>Brindlewood</p>
        <p>482 Elm Parade</p>
        <p>03 9172 5843(P)</p>
      </div>
      <div class="store store--second">
        <p class="store__heading">Kestrelton :</p>
        <p>613 Carlow Road</p>
        <p>03 9238 6014(P)</p>
      </div>
    </div>
  </section>

  <section class="card card--back" aria-label="Business card back">
    <div class="brand brand--large"><span class="brand__mark"></span>KVT Groceries &amp; Spices</div>
    <p class="email-band">email: kvtmarts@mailnest.example</p>
  </section>
</body>
</html>
```